Visitenkarten-Design für Psycho-Kinesiologie Praxis
Zielgruppe
praxis für Psycho-Kinesiologie - Systematische Familienaufstellungen. Einzelsitzungen Gruppentherapie
Ich suche ein Design was auf der einen Seite auffällt, aus dem Rahmen fällt und trotzdem seriös wirkt und Vertrauen schafft.
Die Anhänge sind nur meine Entwürfe also keine fixen Vorgaben
Aufgabenstellung
Eine Seite soll auffallen und Kreativ gestaltet sein
Es gibt ein Template aber die Farben sind noch nicht definiert.
https://www.vorlagenhafen.com/de/demo/48352.html
Es gibt ein Logo (Systemanalytiker) da sind die Farben auch nicht fix Definiert. Gerne sehe ich verschiedene Farbkombinationen
Foto: besseres folgt in kürze
Lumen Harbor Circle: Kann auf einer Seite drauf sein, wenn genug Platz,

```html
<!DOCTYPE html>
<html lang="de">
<head>
<meta charset="utf-8">
<title>Visitenkarten – Seelenweg Praxis</title>
<link rel="stylesheet" href="https://fonts.googleapis.com/css2?family=Montserrat:wght@300;400;600&display=swap">
<style>
  :root {
    --ink: #1a181d;
    --brand-red: #bb0a25;
    --paper: #ffffff;
    --text-dark: #1d1b20;
    --text-light: #ffffff;
    --photo-light: #b8b8b8;
    --photo-dark: #3a3a3a;
  }
  * { box-sizing: border-box; margin: 0; padding: 0; }
  html, body {
    width: 854px; height: 1200px; overflow: hidden;
    background: var(--paper);
    font-family: "Montserrat", sans-serif;
    color: var(--text-dark);
  }
  .sheet { position: relative; width: 854px; height: 1200px; }

  .card {
    position: absolute; width: 313px; height: 202px;
    overflow: hidden;
    box-shadow: 1px 3px 5px rgba(0,0,0,0.25);
  }
  .card--front { left: 101px; background: var(--ink); }
  .card--back { left: 446px; background: var(--paper); }

  .row-1 { top: 97px; } .row-2 { top: 376px; } .row-3 { top: 664px; } .row-4 { top: 933px; }

  .strip-left { position: absolute; left: 0; top: 0; width: 15px; height: 100%; background: var(--brand-red); }
  .band-top { position: absolute; left: 0; top: 0; width: 100%; height: 5px; background: var(--brand-red); }
  .band-bottom { position: absolute; left: 0; bottom: 0; width: 100%; height: 5px; background: var(--brand-red); }

  .dark-panel { position: absolute; left: 156px; top: 0; width: 157px; height: 100%; background: var(--ink); color: var(--text-light); }

  /* Wordmark */
  .wordmark {
    position: absolute; display: flex; align-items: center; gap: 6px;
    transform: translate(-50%, -50%);
    color: var(--text-light); font-weight: 300; white-space: nowrap;
  }
  .wordmark__dot { border-radius: 50%; background: var(--brand-red); flex: none; }
  .wordmark--large { left: 161px; top: 106px; font-size: 36px; letter-spacing: 0.5px; gap: 10px; }
  .wordmark--large .wordmark__dot { width: 14px; height: 14px; }
  .wordmark--small { left: 78px; font-size: 19px; }
  .wordmark--small .wordmark__dot { width: 8px; height: 8px; }

  /* Photo */
  .photo {
    position: absolute;
    background: linear-gradient(160deg, var(--photo-light), #7d7d7d 50%, var(--photo-dark));
    border: 0.5px solid #999;
  }

  /* Services */
  .services { position: absolute; left: 13px; font-size: 6.1px; line-height: 8px; list-style: none; color: var(--text-light); white-space: nowrap; }
  .services li::before, .services .sep { color: var(--brand-red); }
  .services li::before { content: "| "; }
  .services .sep { padding-left: 4px; }
  .services--light { left: 28px; font-size: 7.4px; line-height: 10px; color: var(--text-dark); }
  .services--light .indent { padding-left: 4px; }
  .services--light .indent::before { content: ""; }

  /* Name block */
  .person { position: absolute; line-height: 11px; }
  .person__name { font-weight: 600; font-size: 10px; }
  .person__role { font-weight: 400; font-size: 9px; }
  .person--red .person__name { color: var(--brand-red); }
  .person--light { color: var(--text-light); }
  .person--centered { left: 0; width: 157px; text-align: center; top: 177px; }
  .person--centered .person__name { font-weight: 400; font-size: 12px; }

  /* Contact list */
  .contact { position: absolute; list-style: none; display: flex; flex-direction: column; gap: 5px; font-size: 8px; line-height: 9px; white-space: nowrap; }
  .contact li { position: relative; }
  .contact svg { position: absolute; left: -13px; top: 1.5px; width: 7px; height: 6px; fill: var(--brand-red); }
  .contact--light { color: var(--text-light); }
</style>
</head>
<body>
<svg width="0" height="0" style="position:absolute" aria-hidden="true">
  <symbol id="icon-phone" viewBox="0 0 10 10"><path d="M2.2 0.5 L3.8 2.6 L3 3.6 C3.6 5 4.8 6.3 6.3 7 L7.3 6.2 L9.4 7.8 L8.4 9.5 C4.5 9 1 5.5 0.5 1.5 Z"/></symbol>
  <symbol id="icon-mail" viewBox="0 0 10 8"><path d="M0 0 H10 V8 H0 Z M0.8 0.8 L5 4.3 L9.2 0.8 M0.8 7.2 L3.8 4 M9.2 7.2 L6.2 4" fill="none" stroke="#bb0a25" stroke-width="1"/></symbol>
  <symbol id="icon-web" viewBox="0 0 10 10"><g fill="none" stroke="#bb0a25" stroke-width="0.9"><circle cx="5" cy="5" r="4.3"/><ellipse cx="5" cy="5" rx="1.8" ry="4.3"/><path d="M0.7 5 H9.3 M1.5 2.7 H8.5 M1.5 7.3 H8.5"/></g></symbol>
</svg>

<main class="sheet">

  <!-- Row 1 -->
  <section class="card card--front row-1">
    <div class="strip-left"></div>
    <div class="wordmark wordmark--large"><span class="wordmark__dot"></span>Seelenweg</div>
  </section>
  <section class="card card--back row-1">
    <div class="strip-left"></div>
    <div class="photo" role="img" aria-label="Porträtfoto von Udo Feldmann" style="left:27px;top:7px;width:80px;height:94px"></div>
    <ul class="contact" style="left:40px;top:124px">
      <li><svg><use href="#icon-phone"/></svg>Schweiz<br>0041 790 555 214</li>
      <li><svg><use href="#icon-phone"/></svg>Deutschland<br>0049 170 555 48 16</li>
      <li><svg><use href="#icon-mail"/></svg>info@seelenweg-praxis.ch</li>
      <li><svg><use href="#icon-web"/></svg>www.seelenweg-praxis.ch</li>
    </ul>
    <div class="dark-panel">
      <div class="wordmark wordmark--small" style="top:45px"><span class="wordmark__dot"></span>Seelenweg</div>
      <ul class="services" style="top:77px">
        <li>Psycho-Kinesiologie (nach Dr. Morwald)</li>
        <li>Neurobiologie <span class="sep">|</span> Mentalfeldtherapie</li>
        <li>Geistiges Familienstellen</li>
      </ul>
      <div class="person person--light" style="left:13px;top:147px">
        <div class="person__name">Udo Feldmann</div>
        <div class="person__role">Systemanalytiker</div>
      </div>
    </div>
  </section>

  <!-- Row 2 -->
  <section class="card card--front row-2">
    <div class="band-top"></div>
    <div class="band-bottom"></div>
    <div class="wordmark wordmark--large"><span class="wordmark__dot"></span>Seelenweg</div>
  </section>
  <section class="card card--back row-2">
    <div class="photo" role="img" aria-label="Porträtfoto von Udo Feldmann" style="left:18px;top:16px;width:80px;height:94px"></div>
    <div class="person person--red" style="left:18px;top:122px">
      <div class="person__name">Udo Feldmann</div>
      <div class="person__role">Systemanalytiker</div>
    </div>
    <div class="dark-panel">
      <div class="wordmark wordmark--small" style="top:46px"><span class="wordmark__dot"></span>Seelenweg</div>
      <ul class="services" style="top:80px">
        <li>Psycho-Kinesiologie (nach Dr. Morwald)</li>
        <li>Neurobiologie <span class="sep">|</span> Mentalfeldtherapie</li>
        <li>Geistiges Familienstellen</li>
      </ul>
      <ul class="contact contact--light" style="left:27px;top:122px">
        <li><svg><use href="#icon-phone"/></svg>Schweiz<br>0041 790 555 214</li>
        <li><svg><use href="#icon-phone"/></svg>Deutschland<br>0049 170 555 48 16</li>
        <li><svg><use href="#icon-mail"/></svg>info@seelenweg-praxis.ch</li>
        <li><svg><use href="#icon-web"/></svg>www.seelenweg-praxis.ch</li>
      </ul>
    </div>
    <div class="band-top"></div>
    <div class="band-bottom"></div>
  </section>

  <!-- Row 3 -->
  <section class="card card--front row-3">
    <div class="strip-left"></div>
    <div class="wordmark wordmark--large"><span class="wordmark__dot"></span>Seelenweg</div>
  </section>
  <section class="card card--back row-3">
    <div class="strip-left"></div>
    <div class="person person--red" style="left:22px;top:79px">
      <div class="person__name">Udo Feldmann</div>
      <div class="person__role">Systemanalytiker</div>
    </div>
    <ul class="contact" style="left:35px;top:124px">
      <li><svg><use href="#icon-phone"/></svg>Schweiz<br>0041 790 555 214</li>
      <li><svg><use href="#icon-phone"/></svg>Deutschland<br>0049 170 555 48 16</li>
      <li><svg><use href="#icon-mail"/></svg>info@seelenweg-praxis.ch</li>
      <li><svg><use href="#icon-web"/></svg>www.seelenweg-praxis.ch</li>
    </ul>
    <div class="dark-panel">
      <div class="wordmark wordmark--small" style="top:46px"><span class="wordmark__dot"></span>Seelenweg</div>
      <div class="photo" role="img" aria-label="Porträtfoto von Udo Feldmann" style="left:43px;top:81px;width:70px;height:79px"></div>
      <ul class="services" style="top:166px">
        <li>Psycho-Kinesiologie (nach Dr. Morwald)</li>
        <li>Neurobiologie <span class="sep">|</span> Mentalfeldtherapie</li>
        <li>Geistiges Familienstellen</li>
      </ul>
    </div>
  </section>

  <!-- Row 4 -->
  <section class="card card--front row-4">
    <div class="strip-left"></div>
    <div class="wordmark wordmark--large"><span class="wordmark__dot"></span>Seelenweg</div>
  </section>
  <section class="card card--back row-4">
    <div class="strip-left"></div>
    <ul class="services services--light" style="top:14px">
      <li>Psycho-Kinesiologie</li>
      <li class="indent">(nach Dr. Morwald)</li>
      <li>Neurobiologie</li>
      <li>Mentalfeldtherapie</li>
      <li>Geistiges Familienstellen</li>
    </ul>
    <ul class="contact" style="left:40px;top:119px">
      <li><svg><use href="#icon-phone"/></svg>Schweiz<br>0041 790 555 214</li>
      <li><svg><use href="#icon-phone"/></svg>Deutschland<br>0049 170 555 48 16</li>
      <li><svg><use href="#icon-mail"/></svg>info@seelenweg-praxis.ch</li>
      <li><svg><use href="#icon-web"/></svg>www.seelenweg-praxis.ch</li>
    </ul>
    <div class="dark-panel">
      <div class="wordmark wordmark--small" style="top:44px"><span class="wordmark__dot"></span>Seelenweg</div>
      <div class="photo" role="img" aria-label="Porträtfoto von Udo Feldmann" style="left:39px;top:81px;width:80px;height:93px"></div>
      <div class="person person--light person--centered">
        <div class="person__name">Udo Feldmann</div>
      </div>
    </div>
  </section>

</main>
</body>
</html>
```